Geschäftspapiere für Lasergravuren
Zielgruppe
Lasergravuren z.B. auf Glas, Holz, Filz, Papier, Acryl, eloxierten Aluminium zu Dekorationszwecken,
Ausschneiden von Elementen z.B. aus Holz, Filz, Papier, Acryl usw. zu Dekorationszwecken mit dem Lasergravierer.
Anfertigung verschiedener Dekorationsartikel,
Zielgruppe: Frauen (mit Familien) aller Altersgruppen, die Freude am Dekorieren und Verschenken haben
Aufgabenstellung
Das vorhandene Logo soll mit eingebunden werden

```html
<!DOCTYPE html>
<html lang="de">
<head>
<meta charset="utf-8">
<title>Lumivera – Briefbogen</title>
<link rel="stylesheet" href="https://fonts.googleapis.com/css2?family=Open+Sans:wght@400&family=Arimo:wght@400&display=swap">
<style>
  :root {
    --gold: #b08644;
    --grey: #6d6d6d;
    --rule: #8a8a8a;
    --paper: #ffffff;
    --backdrop: #ffffff;
  }
  * { margin: 0; padding: 0; box-sizing: border-box; }
  html, body {
    width: 866px; height: 1200px; overflow: hidden;
    background: var(--backdrop);
  }
  .canvas { position: relative; width: 866px; height: 1200px; }
  .sheet {
    position: absolute; left: 26px; top: 26px; width: 827px; height: 1169px;
    background: var(--paper);
    box-shadow: 4px 6px 10px rgba(0,0,0,0.35);
    font-family: "Open Sans", sans-serif;
    color: var(--grey);
  }
  .band { position: absolute; left: 0; width: 100%; }
  .band--gold { background: var(--gold); }
  .band--grey { background: var(--grey); }

  .brand-mark {
    position: absolute; left: 482px; top: 63px; width: 92px; height: 92px;
    border: 1.5px solid var(--gold); border-radius: 50%;
  }
  .brand-divider {
    position: absolute; left: 587px; top: 67px; width: 1px; height: 207px;
    background: var(--rule);
  }
  .brand-name {
    position: absolute; left: 602px; top: 82px;
    font-size: 40px; line-height: 1; color: var(--grey); letter-spacing: 0.5px;
  }
  .address {
    position: absolute; left: 603px; top: 154px;
    font-size: 14.5px; line-height: 19px;
  }
  .contact {
    position: absolute; left: 602px; top: 201px; list-style: none;
    font-size: 14.5px; line-height: 19px;
  }
  .contact li { display: flex; align-items: center; gap: 8px; }
  .contact svg { width: 12px; height: 12px; fill: var(--gold); flex: none; }

  .sender-line {
    position: absolute; left: 87px; top: 208px;
    font-family: "Arimo", sans-serif; font-size: 9.5px; color: #444;
    padding-bottom: 2px; border-bottom: 1px solid var(--rule);
  }
  .sender-line .sep { color: var(--gold); }

  .fold-mark { position: absolute; left: 0; width: 30px; height: 1px; background: var(--gold); }
</style>
</head>
<body>
<div class="canvas">
  <div class="sheet">
    <div class="band band--gold" style="top:0;height:15px"></div>
    <div class="band band--grey" style="top:18px;height:2px"></div>
    <div class="band band--grey" style="top:22px;height:1.5px"></div>
    <div class="band band--gold" style="top:25px;height:3px"></div>

    <div class="brand-mark"></div>
    <div class="brand-divider"></div>
    <div class="brand-name">Lumivera</div>

    <address class="address" style="font-style:normal">
      Lindenweg 14<br>31137 Sonnfeld
    </address>

    <ul class="contact">
      <li><svg viewBox="0 0 12 12"><path d="M2.5 1 L4.5 1 L5.3 3.6 L4 4.6 C4.7 6.1 5.9 7.3 7.4 8 L8.4 6.7 L11 7.5 L11 9.5 C11 10.4 10.3 11 9.5 11 C5 11 1 7 1 2.5 C1 1.7 1.6 1 2.5 1Z"/></svg>040 / 123 45 678</li>
      <li><svg viewBox="0 0 12 12"><path d="M3 1h6v3H3z M1.5 4.5h9a1 1 0 0 1 1 1V9H9.5v2h-7V9H.5V5.5a1 1 0 0 1 1-1z M3.5 8v2h5V8z"/></svg>040 / 123 45 679</li>
      <li><svg viewBox="0 0 12 12"><path d="M6 .5a5.5 5.5 0 1 0 0 11 5.5 5.5 0 0 0 0-11zm0 1.2c.6.6 1.1 1.8 1.3 3.2H4.7C4.9 3.5 5.4 2.3 6 1.7zM1.8 5h1.9c0 .7 0 1.4.1 2H1.8a4.3 4.3 0 0 1 0-2zm2.9 2c-.1-.7-.1-1.4 0-2h2.6c.1.6.1 1.3 0 2zm3.5 0c.1-.6.1-1.3.1-2h1.9a4.3 4.3 0 0 1 0 2zM6 10.3c-.6-.6-1.1-1.8-1.3-3.1h2.6C7.1 8.5 6.6 9.7 6 10.3z"/></svg>www.lumivera.de</li>
      <li><svg viewBox="0 0 12 12"><path d="M1 3h10v7H1z M1 3l5 4 5-4" stroke="#fff" stroke-width=".8"/></svg>post@lumivera.de</li>
    </ul>

    <div class="sender-line">Ahornallee 7 <span class="sep">|</span> 30161 Birkental</div>

    <div class="fold-mark" style="top:410px"></div>
    <div class="fold-mark" style="top:802px"></div>

    <div class="band band--gold" style="top:1136px;height:15px"></div>
    <div class="band band--grey" style="top:1154px;height:3px"></div>
    <div class="band band--grey" style="top:1160px;height:2px"></div>
    <div class="band band--gold" style="top:1164px;height:3px"></div>
  </div>
</div>
</body>
</html>
```